Internal Web Pages for Metricsy Hub

I need internal web pages (Why Metricsy Hub?, What We Offer, Blog, Testimonials) that match the design of the homepage. These do not need to be as long or in-depth as the landing page (provided for reference) but I will need three, maybe four, total pages (I'll select the max number of pages for now, but these will all be simple and short pages). Also attached is our new logo design for the company.

They are to essentially be:
Why Metricsy Hub? - An About Us and Why Choose Us page rolled into one.
What We Offer - A Services type page
Blog - self-explanatory
Testimonials - Customer Reviews and Use Cases

Also, maybe a very simple "Contact Us" page as well.

Target Market(s)

Business professionals that work with data analytics teams

Industry/Entity Type

Data Science

Number of Pages Required

5+ page

Requirements
Must have
• It must match the original design in theme and colors.
Nice to have
• Simple pages that show continuity that flows from the original landing page.
Should not have
• Can not be a different design that does not match the landing page.

```html
<!DOCTYPE html>
<html lang="en">
<head>
<meta charset="utf-8">
<title>Contact Us – Metricsy Hub</title>
<link href="https://fonts.googleapis.com/css2?family=Poppins:wght@300;400;600&family=Inter:wght@400;500;600&family=Roboto:wght@500;700&display=swap" rel="stylesheet">
<style>
:root{
  --brand:#4a4fe0;
  --accent:#ef6c0b;
  --ink:#222;
  --muted:#444;
  --panel:#f4f4f4;
  --footer:#14052e;
  --white:#fff;
}
*{box-sizing:border-box;margin:0;padding:0}
html,body{width:1200px;height:2366px;overflow:hidden;background:#fff;font-family:'Inter',sans-serif;color:var(--ink)}
.site-header{height:87px;display:flex;align-items:center;padding:0 90px}
.brand{display:flex;align-items:center;gap:10px;font-family:'Poppins',sans-serif;font-weight:300;font-size:40px;color:var(--brand)}
.brand-dot{width:40px;height:40px;border-radius:50%;background:var(--brand)}
.nav{display:flex;gap:32px;margin-left:72px;font-family:'Poppins',sans-serif;font-size:17px;color:#444}
.nav .active{color:var(--brand)}
.btn-start{margin-left:auto;background:var(--accent);color:#fff;font-family:'Poppins',sans-serif;font-weight:600;font-size:13px;padding:13px 17px;border-radius:2px;box-shadow:0 3px 5px rgba(0,0,0,.2)}
.hero{position:relative;height:246px}
.hero svg{position:absolute;inset:0}
.hero h1{position:absolute;left:84px;top:52px;font-family:'Poppins',sans-serif;font-weight:300;font-size:40px;color:#fff}
.section-title{text-align:center;font-family:'Poppins',sans-serif;font-weight:300;font-size:40px;color:var(--ink)}
.rule{width:143px;height:2px;background:var(--brand);margin:18px auto 0}
.intro{width:880px;margin:36px auto 0;text-align:center;font-size:15.5px;line-height:24px;color:var(--muted);letter-spacing:-.1px}
.map{width:912px;height:400px;margin:38px auto 0;background:linear-gradient(135deg,#e4e4e4,#d3d3d3 50%,#e6e6e6)}
.contacts{width:912px;margin:50px auto 0;display:flex;height:60px}
.contact{display:flex;align-items:center;gap:22px;font-size:16px;line-height:21px;color:var(--ink);font-weight:500}
.contact svg{flex:none}
.form-panel{width:912px;margin:40px auto 0;background:var(--panel);height:572px;padding-top:36px}
.form-panel .rule{width:70px;margin-top:16px}
.form-grid{width:740px;margin:40px auto 0;display:grid;grid-template-columns:1fr 1fr;gap:22px 24px}
.field{height:51px;background:#fff;box-shadow:0 2px 5px rgba(0,0,0,.12);padding:0 20px;display:flex;align-items:center;font-size:16px;color:#444}
.field.wide{grid-column:span 2;height:68px;align-items:flex-start;padding-top:16px}
.submit{display:block;width:208px;height:50px;margin:42px auto 0;background:var(--brand);color:#fff;font-family:'Roboto',sans-serif;font-weight:700;font-size:16px;text-align:center;line-height:50px}
.footer{position:absolute;top:1840px;left:0;width:1200px;height:526px;background:var(--footer);color:#fff}
.f-col{position:absolute;top:62px}
.f-brand{font-family:'Poppins',sans-serif;font-weight:300;font-size:38px;display:flex;gap:10px;align-items:center}
.f-brand span.sq{width:36px;height:36px;border-radius:50%;background:#fff}
.f-text{font-size:16px;line-height:22px;margin-top:26px;width:290px}
.socials{display:flex;gap:7px;margin-top:20px}
.socials span{width:35px;height:35px;border:1.5px solid #fff;border-radius:50%}
.f-head{font-family:'Roboto',sans-serif;font-weight:700;font-size:19px;letter-spacing:.3px}
.f-item{display:flex;gap:18px;margin-top:22px;font-family:'Roboto',sans-serif;font-weight:500;font-size:16px;line-height:22px;letter-spacing:.6px}
.sub-text{font-size:14.5px;line-height:24px;margin-top:28px;width:310px}
.email-box{width:303px;height:40px;background:#fff;color:#555;font-size:14px;padding:0 18px;line-height:40px;margin-top:22px;border-radius:2px}
.btn-sub{display:inline-block;background:var(--accent);font-family:'Roboto',sans-serif;font-weight:700;font-size:15px;padding:0 24px;height:40px;line-height:40px;margin-top:17px}
.copyright{position:absolute;top:460px;width:100%;text-align:center;font-size:16px;font-weight:500}
</style>
</head>
<body>
<header class="site-header">
  <div class="brand"><span class="brand-dot"></span>Metricsy Hub</div>
  <nav class="nav"><span>Home</span><span>About us</span><span class="active">Our Service</span><span>Blog</span><span>Contact</span></nav>
  <span class="btn-start">GET STARTED</span>
</header>
<section class="hero">
  <svg width="1200" height="246" viewBox="0 0 1200 246" role="img" aria-label="Photo of two business colleagues smiling at a laptop">
    <defs><linearGradient id="hg" x1="0" x2="1"><stop offset="0" stop-color="#5a5a5c"/><stop offset=".5" stop-color="#6e6a68"/><stop offset="1" stop-color="#4a4c50"/></linearGradient></defs>
    <polygon points="0,0 1200,0 1200,133 413,226 0,136" fill="url(#hg)"/>
    <polygon points="110,160 413,246 1000,157 413,226" fill="var(--brand)"/>
  </svg>
  <h1>Contact Us</h1>
</section>
<h2 class="section-title" style="margin-top:62px">Get In Touch</h2>
<div class="rule"></div>
<p class="intro">Sed ut perspiciatis unde omnis iste natus error sit voluptatem accusantium doloremque laudantium, totam rem aperiam, eaque ipsa quae ab illo inventore veritatis et quasi architecto beatae vitae dicta sunt explicabo. Nemo enim ipsam vptatem quia voluptas sit aspernatur aut odit aut fugit, sed quia consequuntur magni dolores eos qui ratione voluptatem sequi nesciunt. Neque porro quisquam est, qui dolorem ipsum quia dolor sit amet, consectetur, adipisci velit, sed quia non numquam eius modi tempora incidunt ut labore et dolore magnam aliquam quaerat voluptatem</p>
<div class="map" role="img" aria-label="Greyscale street map showing the office location"></div>
<div class="contacts">
  <div class="contact" style="width:378px"><svg width="54" height="54" viewBox="0 0 54 54"><circle cx="27" cy="27" r="25" fill="none" stroke="#222" stroke-width="1.5"/><path d="M27 15a8 8 0 0 0-8 8c0 6 8 15 8 15s8-9 8-15a8 8 0 0 0-8-8z" fill="var(--brand)"/><circle cx="27" cy="23" r="3" fill="#fff"/></svg><div>Metricsy Hub<br>41 Ledger Lane, Suite 12<br>Northfield Park</div></div>
  <div class="contact" style="width:273px"><svg width="54" height="54" viewBox="0 0 54 54"><circle cx="27" cy="27" r="25" fill="none" stroke="#222" stroke-width="1.5"/><path d="M18 17l5-2 3 7-3 2c1 3 4 6 7 7l2-3 7 3-2 5c-10 0-19-9-19-19z" fill="var(--brand)"/></svg><div>Phone<br>555 0142 7788</div></div>
  <div class="contact"><svg width="54" height="54" viewBox="0 0 54 54"><circle cx="27" cy="27" r="25" fill="none" stroke="#222" stroke-width="1.5"/><rect x="15" y="19" width="24" height="17" rx="2" fill="var(--brand)"/><path d="M15 21l12 8 12-8" fill="none" stroke="#fff" stroke-width="1.5"/></svg><div>Email<br>hello@metricsyhub.com</div></div>
</div>
<section class="form-panel">
  <h2 class="section-title">Contact Form</h2>
  <div class="rule"></div>
  <div class="form-grid">
    <div class="field">Your name</div><div class="field">Company</div>
    <div class="field">Email address</div><div class="field">Location</div>
    <div class="field">Phone</div><div class="field">Subject</div>
    <div class="field wide">Message</div>
  </div>
  <span class="submit">SUBMIT</span>
</section>
<footer class="footer">
  <div class="f-col" style="left:140px">
    <div class="f-brand"><span class="sq"></span>Metricsy Hub</div>
    <p class="f-text">Sed ut perspiciatis unde omnis iste natus error sit voluptatem accusantium dolorque laudantium, totam rem aperiam, eaque ipsa quae ab illo inventore veritatis et quasi</p>
    <div class="socials"><span></span><span></span><span></span><span></span></div>
  </div>
  <div class="f-col" style="left:477px;top:70px">
    <div class="f-head">CONTACT US</div>
    <div class="f-item"><svg width="20" height="24" viewBox="0 0 20 24"><path d="M10 2a7 7 0 0 0-7 7c0 5 7 13 7 13s7-8 7-13a7 7 0 0 0-7-7z" fill="none" stroke="#fff" stroke-width="1.4"/><circle cx="10" cy="9" r="2.5" fill="none" stroke="#fff" stroke-width="1.4"/></svg><div>Metricsy Hub<br>41 Ledger Lane,<br>Suite 12</div></div>
    <div class="f-item"><svg width="20" height="22" viewBox="0 0 20 22"><path d="M3 3l4-1 2 5-2 2c1 3 3 5 6 6l2-2 5 2-1 4C10 19 3 12 3 3z" fill="none" stroke="#fff" stroke-width="1.3"/></svg><div>Phone :<br>555-0142-7788</div></div>
    <div class="f-item"><svg width="20" height="20" viewBox="0 0 20 20"><rect x="1" y="4" width="18" height="12" fill="none" stroke="#fff" stroke-width="1.3"/><path d="M1 4l9 7 9-7" fill="none" stroke="#fff" stroke-width="1.3"/></svg><div>Email :<br>hello@metricsyhub.com</div></div>
  </div>
  <div class="f-col" style="left:751px;top:67px">
    <div class="f-head">SIGN UP TO RECEIVE EMAIL</div>
    <p class="sub-text">Excepteur sint occaecat cupidatat non proident, sunt in culpa qui Nemo enim ipsam</p>
    <div class="email-box">Enter Email</div>
    <span class="btn-sub">SUBSCRIBE</span>
  </div>
  <p class="copyright">Copyright © Metricsy Hub 2021. All rights reserved. | Privacy Policy</p>
</footer>
</body>
</html>
```